WEB PAGES DESIGN

We need a web design for a new company called "NEXO47". Our major business is that provide Internet Data Center solution, such as: rack/colocation, bandwidth, dedicated server, cloud server, CDN, and so on.
Requirements of Design:
1. Home page layout can refer to index-content.jpg in the attachments, but not limited.
2. According to match logo colors to design colors of web pages, Logo in the attachments.
3. The web contents of home page in image of the index-content.jpg.
4. The successful bidder will need to design three banner.

```html
<!DOCTYPE html>
<html lang="en">
<head>
<meta charset="utf-8">
<title>NEXO47 – IDC Solutions</title>
<link href="https://fonts.googleapis.com/css2?family=Lato:wght@300;400;700&family=Arimo:wght@400;700&display=swap" rel="stylesheet">
<style>
  :root {
    --green: #78bd3c;
    --green-dark: #5e9e2a;
    --ink: #3a3a3a;
    --text: #555;
    --muted: #8a8a8a;
    --soft-bg: #f5f5f5;
    --bar-bg: #efefef;
    --line: #e2e2e2;
    --white: #fff;
  }
  * { margin: 0; padding: 0; box-sizing: border-box; }
  html, body { width: 976px; height: 1200px; overflow: hidden; background: var(--white); }
  body { position: relative; font-family: "Arimo", Arial, sans-serif; color: var(--text); }
  .abs { position: absolute; }

  .top-strip { left: 0; top: 0; width: 976px; height: 20px; background: var(--soft-bg); }
  .site-header { left: 0; top: 20px; width: 976px; height: 47px; background: var(--white); }
  .brand { left: 197px; top: 29px; display: flex; align-items: center; gap: 8px; }
  .brand-square { width: 26px; height: 26px; background: var(--green); }
  .brand-name { font-family: "Lato", sans-serif; font-weight: 700; font-size: 24px; color: var(--ink); letter-spacing: 1px; }
  .main-nav a { position: absolute; top: 40px; font-size: 8.5px; color: var(--text); text-decoration: none; white-space: nowrap; }
  .main-nav a.is-active { color: var(--green); }
  .nav-underline { left: 456px; top: 64px; width: 24px; height: 3px; background: var(--green); }

  .hero { left: 0; top: 67px; width: 976px; height: 293px;
    background:
      radial-gradient(ellipse 22% 30% at 50% 18%, rgba(235,235,235,0.85), rgba(235,235,235,0) 100%),
      radial-gradient(ellipse 40% 60% at 50% 55%, rgba(190,190,190,0.9), rgba(190,190,190,0) 100%),
      linear-gradient(90deg, #2a2a2a 0%, #4a4a4a 12%, #3a3a3a 22%, #8c8c8c 40%, #a8a8a8 50%, #8c8c8c 60%, #3a3a3a 78%, #4a4a4a 88%, #2a2a2a 100%); }
  .hero-title { left: 0; top: 172px; width: 976px; text-align: center; font-family: "Lato", sans-serif; font-weight: 400; font-size: 27px; color: var(--white); }
  .hero-text { left: 0; top: 213px; width: 976px; text-align: center; font-family: "Lato", sans-serif; font-weight: 700; font-size: 12.4px; line-height: 16px; color: var(--white); }
  .hero-link { left: 0; top: 256px; width: 976px; text-align: center; font-family: "Lato", sans-serif; font-weight: 700; font-size: 8.5px; letter-spacing: 0.6px; color: #e8e8e8; }

  .products { left: 0; top: 360px; width: 976px; height: 272px; background: var(--soft-bg); }
  .section-title { width: 976px; left: 0; text-align: center; font-family: "Lato", sans-serif; font-weight: 300; font-size: 14.5px; letter-spacing: 1px; color: var(--ink); }
  .section-sub { width: 976px; left: 0; text-align: center; font-size: 7.8px; color: var(--text); }
  .product { width: 140px; text-align: center; }
  .product svg { display: block; margin: 0 auto; }
  .product-label { margin-top: 10px; font-family: "Lato", sans-serif; font-weight: 700; font-size: 7.8px; letter-spacing: 0.8px; color: var(--ink); }

  .partner-badge { left: 367px; top: 763px; width: 226px; height: 53px; border-radius: 27px; background: linear-gradient(90deg, #9fcf6f, #c4e3a3); }
  .slider-arrow { top: 869px; font-size: 12px; color: var(--muted); }
  .slider-dots { left: 456px; top: 873px; display: flex; gap: 2px; }
  .slider-dots span { width: 5px; height: 5px; border-radius: 50%; background: #999; }
  .slider-dots span.is-current { background: var(--green); }

  .footer-rule { left: 0; top: 924px; width: 976px; height: 1px; background: var(--line); }
  .footer-shadow { left: 336px; top: 925px; width: 288px; height: 8px; border-radius: 50%; background: radial-gradient(ellipse at 50% 0%, rgba(0,0,0,0.18), rgba(0,0,0,0) 70%); }

  .footer-brand { left: 196px; top: 972px; width: 56px; text-align: center; }
  .footer-brand-square { width: 42px; height: 42px; margin: 0 auto 6px; background: var(--green); }
  .footer-brand-name { font-family: "Lato", sans-serif; font-weight: 700; font-size: 10px; color: var(--ink); }

  .footer-heading { top: 966px; font-family: "Lato", sans-serif; font-weight: 300; font-size: 14px; letter-spacing: 0.8px; color: #666; }
  .contact-item { left: 270px; display: flex; gap: 8px; font-size: 7.8px; line-height: 10px; color: var(--text); }
  .contact-item svg { flex: none; margin-top: 1px; }
  .contact-item.is-strong { font-weight: 700; color: #444; }

  .news-item { left: 452px; width: 166px; height: 38px; display: flex; align-items: flex-start; border-bottom: 1px solid var(--line); }
  .news-date { width: 30px; text-align: center; border-right: 1px solid var(--line); height: 30px; }
  .news-day { display: block; font-family: "Lato", sans-serif; font-size: 15px; line-height: 15px; color: #777; }
  .news-month { display: block; font-size: 6.5px; color: var(--muted); letter-spacing: 0.5px; }
  .news-text { padding-left: 8px; padding-top: 2px; font-size: 6.5px; line-height: 9px; letter-spacing: 0.4px; color: var(--muted); text-transform: uppercase; }

  .chat-brand { left: 680px; top: 976px; display: flex; align-items: center; gap: 6px; }
  .chat-dot { width: 16px; height: 16px; border-radius: 50%; background: var(--green); }
  .chat-name { font-family: "Arimo", sans-serif; font-weight: 700; font-size: 13px; color: var(--green); }

  .bottom-bar { left: 0; top: 1169px; width: 976px; height: 31px; background: var(--bar-bg); }
  .copyright { left: 197px; top: 1182px; font-size: 7.2px; color: var(--muted); }
  .legal-links { right: 209px; top: 1182px; font-size: 7.2px; color: var(--muted); }
</style>
</head>
<body>
  <div class="abs top-strip"></div>

  <header class="abs site-header"></header>
  <div class="abs brand"><span class="brand-square"></span><span class="brand-name">NEXO47</span></div>
  <nav class="main-nav">
    <a class="is-active" style="left:458px">Home</a>
    <a style="left:497px">Dedicated Server</a>
    <a style="left:576px">Hosting</a>
    <a style="left:623px">Data Center</a>
    <a style="left:685px">About Us</a>
    <a style="left:730px">Contact Us</a>
  </nav>
  <div class="abs nav-underline"></div>

  <section class="abs hero" role="img" aria-label="Photograph of a data center corridor lined with server racks under ceiling lights"></section>
  <h1 class="abs hero-title">IDC Solutions</h1>
  <p class="abs hero-text">NEXO47 provides a wide range of highly specialized solutions that utilizes<br>technology to transform your organisation.</p>
  <div class="abs hero-link">LEARN MORE</div>

  <section class="abs products"></section>
  <h2 class="abs section-title" style="top:401px">OUR PRODUCTS</h2>
  <p class="abs section-sub" style="top:423px">Duis aute irure dolor in reprehenderit in voluptate velit esse cillum dolore eu fugiat nulla pariatur</p>

  <div class="abs product" style="left:192px;top:455px">
    <svg width="96" height="110" viewBox="0 0 96 110"><polygon points="48,2 94,28 94,82 48,108 2,82 2,28" fill="#fff" stroke="#78bd3c" stroke-width="2"/>
      <g fill="#78bd3c"><rect x="34" y="38" width="28" height="8" rx="3"/><rect x="34" y="49" width="28" height="8" rx="3"/><rect x="34" y="60" width="28" height="8" rx="3"/><rect x="47" y="68" width="2" height="6"/><rect x="32" y="74" width="32" height="2"/></g></svg>
    <div class="product-label">DEDICATED SERVER</div>
  </div>
  <div class="abs product" style="left:332px;top:455px">
    <svg width="96" height="110" viewBox="0 0 96 110"><polygon points="48,2 94,28 94,82 48,108 2,82 2,28" fill="#fff" stroke="#78bd3c" stroke-width="2"/>
      <path d="M28 66 a10 10 0 0 1 2-19 a14 14 0 0 1 27-4 a11 11 0 0 1 11 23 z" fill="none" stroke="#78bd3c" stroke-width="3"/>
      <g fill="#78bd3c"><rect x="40" y="49" width="17" height="4" rx="2"/><rect x="40" y="55" width="17" height="4" rx="2"/><rect x="40" y="61" width="17" height="4" rx="2"/></g></svg>
    <div class="product-label">SERVER HOSTING</div>
  </div>
  <div class="abs product" style="left:476px;top:455px">
    <svg width="96" height="110" viewBox="0 0 96 110"><polygon points="48,2 94,28 94,82 48,108 2,82 2,28" fill="#fff" stroke="#78bd3c" stroke-width="2"/>
      <circle cx="48" cy="55" r="20" fill="#78bd3c"/><circle cx="48" cy="55" r="15" fill="#fff"/><rect x="47" y="44" width="2" height="12" fill="#78bd3c"/><circle cx="48" cy="56" r="2.5" fill="#78bd3c"/></svg>
    <div class="product-label">RACK &amp; BANDWIDTH</div>
  </div>
  <div class="abs product" style="left:627px;top:455px">
    <svg width="96" height="110" viewBox="0 0 96 110"><polygon points="48,2 94,28 94,82 48,108 2,82 2,28" fill="#fff" stroke="#78bd3c" stroke-width="2"/>
      <g fill="#78bd3c"><circle cx="36" cy="46" r="5"/><circle cx="60" cy="46" r="5"/><circle cx="48" cy="44" r="6"/><path d="M27 64 a9 9 0 0 1 18 0z"/><path d="M51 64 a9 9 0 0 1 18 0z"/><path d="M37 66 a11 11 0 0 1 22 0z"/></g></svg>
    <div class="product-label">RESELLER &amp; REFEERAL</div>
  </div>

  <h2 class="abs section-title" style="top:677px">OUR PPARTNERS</h2>
  <p class="abs section-sub" style="top:698px">Duis aute irure dolor in reprehenderit in voluptate velit esse cillum dolore eu fugiat nulla pariatur</p>
  <div class="abs partner-badge" role="img" aria-label="Partner badge for a manpower services company"></div>

  <div class="abs slider-arrow" style="left:439px">&#8249;</div>
  <div class="abs slider-dots"><span class="is-current"></span><span></span><span></span><span></span><span></span><span></span><span></span><span></span></div>
  <div class="abs slider-arrow" style="left:518px">&#8250;</div>

  <div class="abs footer-rule"></div>
  <div class="abs footer-shadow"></div>

  <div class="abs footer-brand"><div class="footer-brand-square"></div><div class="footer-brand-name">NEXO47</div></div>

  <h3 class="abs footer-heading" style="left:269px">CONTACT US</h3>
  <div class="abs contact-item" style="top:993px">
    <svg width="6" height="8" viewBox="0 0 6 8"><path d="M3 0a3 3 0 0 1 3 3c0 2-3 5-3 5S0 5 0 3a3 3 0 0 1 3-3z" fill="#777"/></svg>
    <span>#123, Street Name, City Name<br>Country 1234</span></div>
  <div class="abs contact-item is-strong" style="top:1021px">
    <svg width="7" height="7" viewBox="0 0 7 7"><path d="M1 0l1.5 1.8-.8 1a4 4 0 0 0 1.5 1.5l1-.8L6 5l-.7 1.5C2.5 6.5.5 4.5.5.7z" fill="#777"/></svg>
    <span>70 5550 1234</span></div>
  <div class="abs contact-item" style="top:1040px">
    <svg width="8" height="7" viewBox="0 0 8 7"><ellipse cx="4" cy="3" rx="4" ry="2.6" fill="#777"/></svg>
    <span>Live Chat</span></div>
  <div class="abs contact-item" style="top:1059px">
    <svg width="7" height="7" viewBox="0 0 7 7"><circle cx="3.5" cy="3.5" r="3" fill="none" stroke="#777"/></svg>
    <span>Support Online</span></div>

  <h3 class="abs footer-heading" style="left:458px">LATEST NEWS</h3>
  <div class="abs news-item" style="top:994px"><div class="news-date"><span class="news-day">10</span><span class="news-month">MAY</span></div><div class="news-text">Duis aute irure dolor in<br>reprehenderit in voluptate</div></div>
  <div class="abs news-item" style="top:1032px"><div class="news-date"><span class="news-day">18</span><span class="news-month">MAY</span></div><div class="news-text">Duis aute irure dolor in<br>reprehenderit in voluptate</div></div>
  <div class="abs news-item" style="top:1070px"><div class="news-date"><span class="news-day">21</span><span class="news-month">JUN</span></div><div class="news-text">Duis aute irure dolor in<br>reprehenderit in voluptate</div></div>
  <div class="abs news-item" style="top:1108px;border-bottom:none"><div class="news-date"><span class="news-day">24</span><span class="news-month">AUG</span></div><div class="news-text">Duis aute irure dolor in<br>reprehenderit in voluptate</div></div>

  <div class="abs chat-brand"><span class="chat-dot"></span><span class="chat-name">Chatly</span></div>

  <footer class="abs bottom-bar"></footer>
  <div class="abs copyright">Copyright © 2015 Nexo47</div>
  <div class="abs legal-links">Terms of Services &nbsp;|&nbsp; Privacy Policy &nbsp;|&nbsp; Contact Us</div>
</body>
</html>
```